Banner for a program to be used as a cover photo for Facebook

Banner design for a program I run called: The Craft of Swift Bloom
This is a 90 day implementation program for business owners who set one main goal to reach during that time. The focus of the program is to help them set the goal, create the strategy to reach the goal and take keystone actions to achieve the goal. This program (I run multiple at a time) is exclusive to only 8 people at a time...the price point of the program is $6,000.

Company Name: Woven Horizon

My title: Business Acceleration Mentor (BAM!)

My area of expertise: Helping business owners who already know what they do, who they serve, and have momentum (and sales) accelerate the growth of their business by eliminate what they don't need and simplifying the strategy to achieve mind blowing results. (Success habits, behaviors, routines, attitudes, speed of implementation, simplification, essentialism, focus, goal setting, high performance)

Who I want to attract: People who have made $25k - $75k in the last 12 months of their business (service based) who are action takers, big thinkers, in it to win it, take action even in the face of fear, committed, decision makers

Target Market(s)

Women business owners who have been in business for 2 - 5 years making at least $25k - $75k in their previous 12 months. They are feminine, married, moms, higher end and looking for a more exclusive and selective group of like-minded people to grow with. They are attracted to a more glamorous, boutique feel and desire to catapult the results in their business.

Industry/Entity Type

Business

Font styles to use
Sans Serif

Requirements
Must have
• Crisp, Clean, High End, Simple, Elegant, Picture of me
• Text on Banner:
• The Craft of Swift Bloom
• with Clara Westby, Business Acceleration Mentor
Should not have
• Men in suits in pictures.
• Corporate Feel.

```html
<!DOCTYPE html>
<html lang="en">
<head>
<meta charset="utf-8">
<title>The Craft of Swift Bloom — Cover Banner</title>
<link rel="stylesheet" href="https://fonts.googleapis.com/css2?family=Montserrat:wght@400;700&family=Crimson+Pro:ital,wght@1,500&display=swap">
<style>
  :root {
    --page: #ffffff;
    --slate: #555b63;
    --slate-dark: #4a5058;
    --frame-line: rgba(255, 255, 255, 0.35);
    --title-white: #ffffff;
    --accent-yellow: #f5d523;
    --subtitle: #f3f3f3;
    --hair: #d9bf86;
    --skin: #e7c3ad;
    --garment: #eeeae4;
  }
  html, body {
    margin: 0;
    padding: 0;
    width: 1200px;
    height: 1080px;
    overflow: hidden;
    background: var(--page);
  }
  .canvas {
    position: relative;
    width: 1200px;
    height: 1080px;
  }
  .banner {
    position: absolute;
    left: 108px;
    top: 353px;
    width: 984px;
    height: 374px;
    background: linear-gradient(90deg, var(--slate-dark) 0%, var(--slate) 45%, var(--slate) 75%, var(--slate-dark) 100%);
    overflow: hidden;
  }
  .portrait {
    position: absolute;
    left: 444px;
    top: 0;
    width: 480px;
    height: 374px;
    background:
      radial-gradient(ellipse 26% 38% at 50% 48%, var(--skin) 0%, rgba(231,195,173,0.85) 55%, rgba(231,195,173,0) 100%),
      radial-gradient(ellipse 42% 62% at 50% 52%, var(--hair) 0%, rgba(217,191,134,0.7) 60%, rgba(217,191,134,0) 100%),
      linear-gradient(180deg, rgba(0,0,0,0) 82%, var(--garment) 100%);
  }
  .inner-frame {
    position: absolute;
    left: 13px;
    top: 12px;
    right: 13px;
    bottom: 12px;
    border: 1px solid var(--frame-line);
    pointer-events: none;
  }
  .title-box {
    position: absolute;
    left: 55px;
    top: 103px;
    width: 408px;
    height: 91px;
    border: 1px solid var(--frame-line);
    box-sizing: border-box;
  }
  .title-kicker {
    position: absolute;
    left: 50%;
    top: -18px;
    transform: translateX(-50%);
    padding: 0 14px;
    background: var(--slate);
    font-family: "Montserrat", sans-serif;
    font-weight: 400;
    font-size: 29px;
    letter-spacing: 2.5px;
    line-height: 36px;
    color: var(--title-white);
    white-space: nowrap;
  }
  .title-main {
    position: absolute;
    left: 0;
    right: 0;
    top: 30px;
    text-align: center;
    font-family: "Montserrat", sans-serif;
    font-weight: 700;
    font-size: 45px;
    letter-spacing: 0.5px;
    line-height: 50px;
    color: var(--accent-yellow);
    white-space: nowrap;
  }
  .byline {
    position: absolute;
    left: 40px;
    width: 438px;
    top: 207px;
    text-align: center;
    font-family: "Crimson Pro", serif;
    font-style: italic;
    font-weight: 500;
    font-size: 25px;
    line-height: 34px;
    color: var(--subtitle);
  }
</style>
</head>
<body>
  <div class="canvas">
    <section class="banner">
      <div class="portrait" role="img" aria-label="Portrait photo of Clara Westby, smiling, with shoulder-length wavy blonde hair"></div>
      <div class="inner-frame"></div>
      <div class="title-box">
        <span class="title-kicker">THE CRAFT OF</span>
        <h1 class="title-main" style="margin:0">SWIFT BLOOM</h1>
      </div>
      <p class="byline" style="margin:0">with Clara Westby,<br>Business Acceleration Mentor</p>
    </section>
  </div>
</body>
</html>
```